Plumbing Trifold Design for Restoration Company

We would like this brochure to match our current KWT branding and marketing materials. The overall look should feel modern, clean, premium, and trustworthy.

Our brand colors are included in the attached files along with a picture of what our current marketing material looks like. We'd like to use real KWT photography whenever possible rather than stock images, but if stock images are necessary, please go ahead and use.

The brochure should communicate that KWT is a full-service plumbing company backed by years of experience in both traditional plumbing and complex pipe restoration.

Front Page: we would like to include logo, phone number (800-391-2857), website (www.kwtflowline.example) and then maybe the following: "Traditional Plumbing Services", "residential & commercial, 24/7 Emergency Service, Licensed & Insured" and can also add "reliable Repairs. Honest Service. Lasting Solutions" if spacing allows.

Other sections we would like included (not in any particular order):

-Why Choose KWT?:
Family-oriented team
Licensed & insured professionals
Residential & commercial expertise
Honest recommendations
Quality workmanship
Emergency service available
Clean, respectful technicians
One trusted company for plumbing and sewer solutions
____________________________
Our Story:
Built on solving complex plumbing challenges. Trusted for every plumbing need.
Since our founding, Conduit Renewal Services has built a reputation for helping homeowners, businesses, and property managers solve some of the industry’s most challenging plumbing and sewer problems through quality workmanship, professionalism, and innovative solutions.
As our customers’ needs have grown, so has our commitment to serving them. What began as a leader in pipe restoration has expanded into full-service plumbing, allowing us to provide complete plumbing solutions—from everyday repairs and fixture replacements to water heaters, drain cleaning, repiping, and emergency plumbing services.
Today, our traditional plumbing division delivers the same level of expertise, communication, and customer care that KWT has become known for. Whether it’s a simple repair or a complex plumbing project, our goal remains the same: to provide dependable solutions, lasting quality, and an exceptional customer experience every step of the way.
-Our Values:
The KWT Way
Professional - Don't settle for good, BE GREAT
Responsive - When there's a need, BE FIRST!
Service - Life is not about you, BE ABOUT OTHERS!
These three values guide everything we do
Complete Plumbing Solutions:
-Plumbing Repairs
Reliable solutions to keep your plumbing system running safely and efficiently.
Leak detection & repair
Pipe Burst Repairs
Water line repairs
Whole-home repiping

-Fixtures & Installations
Professional installation, repair, and replacement of the fixtures you use every day.
Faucets
Toilets
Sinks
Showers & tubs
Garbage disposals
Hose bibs
Shut-off valves

-Water Heater Services
Whether you need a repair, replacement, or routine maintenance, we'll keep your hot water flowing.
Water heater repair
Water heater replacement
Tankless water heaters
Expansion tanks
Recirculation pumps
Preventative maintenance

-Drain & Sewer Solutions
From routine drain cleaning to complete sewer repairs, our team has the equipment and expertise to get your plumbing flowing again.
Drain cleaning
Hydro jetting
Camera inspections
Main sewer line cleaning
Sewer line repair
Sewer line replacement
Emergency drain backups
maybe add in a blurb saying
"Need a Trenchless Solution?
Ask about our non-invasive solutions as an alternative to traditional replacement for sewer and storm drain systems"
Testimonials:
"This company is fantastic, very professional and knowledgeable. Use them at several of my communities I manage and highly recommend them!" Belmoro Townhomes
"KWT continues to be the primary plumbing vendor I use for all of my properties throughout Tampa Bay!" Corvallo Dunes Condominium
"KWT did a great job at a great price and have always been willing to help with their abundance of knowledge prior to even working on projects for our community!" Townhomes at Heron Pond
"KWT is amazing! My office flooded out on a Friday night and they responded within a couple hours to make the needed repair. The team was professional and got right to work (there van was also immaculate, which tells you a lot about hot they operate). Would definitely recommend them to anyone!" Dawsen Pruitt
______________________
Ready to get started?
Whether it's a leaking pipe, a new water heater, a clogged drain, or a plumbing emergency, our team is here to help
800-391-2857
info@kwtflowline.example
www.kwtflowline.example

Additional Information: please feel free to edit any of the pictures provided and AI files can be provided for the other marketing material if helpful. We would like an AI file and PDF ready print if possible.
Thank you!

Target Market(s)

commercial and residential property owners

Industry/Entity Type

Plumbing

Colors
0054AA
0677BA
7BADD7
CADEEF
E8F1F8

Requirements
Must have
• My project must flow with current marketing material colors
Nice to have
• would like the front page picture to fade nicely into background

```html
<!DOCTYPE html>
<html lang="en">
<head>
<meta charset="utf-8">
<title>KWT Traditional Plumbing Trifold</title>
<link rel="stylesheet" href="https://fonts.googleapis.com/css2?family=Russo+One&family=Arimo:wght@400;700&display=swap">
<style>
:root{
  --navy:#1d2130;
  --navy-2:#242a3b;
  --line:#333b52;
  --blue-deep:#0054aa;
  --blue:#0677ba;
  --blue-bright:#1e8fe0;
  --blue-soft:#7badd7;
  --blue-pale:#cadeef;
  --ice:#e8f1f8;
  --white:#ffffff;
  --ink:#1d2130;
  --stage:#d6d8db;
  --head:"Russo One",sans-serif;
  --body:"Arimo",sans-serif;
}
*{box-sizing:border-box;margin:0;padding:0}
html,body{width:1200px;height:3423px;overflow:hidden}
body{background:var(--stage);font-family:var(--body);color:var(--ink);position:relative}
.spread{position:absolute;left:50px;width:1100px;height:780px;display:flex;box-shadow:0 6px 18px rgba(0,0,0,.18)}
.spread--outside{top:900px}
.spread--inside{top:1740px}
.panel{width:367px;height:100%;position:relative;display:flex;flex-direction:column}
.panel--right{width:366px}
.dark{background:var(--navy);color:var(--white)}
.band{background:linear-gradient(90deg,var(--blue-deep),var(--blue-bright))}
.ph{display:block}

/* trenchless */
.trench{height:217px;padding:30px 28px 0 34px}
.trench__row{display:flex;gap:16px;align-items:flex-start}
.badge{width:70px;height:72px;border:2px solid var(--blue-bright);color:var(--blue-bright);font-family:var(--head);text-align:center;line-height:1;padding-top:6px;flex:none}
.badge b{display:block;font-size:26px;font-weight:400}
.badge span{display:block;font-size:10px;margin-top:3px}
.trench h2{font-family:var(--head);font-weight:400;font-size:28px;line-height:1.08}
.trench h2 em{font-style:normal;color:var(--blue-bright)}
.trench p{font-size:13px;line-height:1.4;margin-top:18px}

/* why choose */
.why{flex:1;background:var(--white);color:var(--ink);padding:34px 30px 0 32px;display:flex;flex-direction:column}
.why h2{font-family:var(--head);font-weight:400;font-size:25px;color:var(--blue-deep);margin-bottom:14px}
.why ul{list-style:none}
.why li{font-size:15px;font-weight:700;color:var(--ink);padding-left:24px;position:relative;line-height:36.5px}
.why li::before{content:"";position:absolute;left:2px;top:13px;border-left:10px solid var(--blue-deep);border-top:6px solid transparent;border-bottom:6px solid transparent}
.why p{font-size:15px;line-height:1.25;margin-top:8px;color:var(--ink)}
.why .van{margin:auto -30px 0 -32px;height:150px;background:linear-gradient(180deg,#f4f5f7,#c9ccd3)}

/* get started */
.start{padding:30px 30px 0;text-align:center;flex:1}
.start h2{font-family:var(--head);font-weight:400;font-size:31px;line-height:1.05}
.start h2 em{font-style:normal;color:var(--blue-bright);display:block;font-size:33px}
.start .lead{font-size:12.5px;line-height:1.45;margin:14px 10px 0}
.testi h3{font-family:var(--head);font-weight:400;font-size:29px;color:var(--blue-bright);margin:34px 0 20px}
.quote{border:1px solid var(--line);border-radius:6px;background:var(--navy-2);padding:16px 18px 12px;margin-bottom:20px;font-size:12px;line-height:1.35}
.quote cite{display:block;font-style:normal;font-weight:700;font-size:14px;color:var(--blue-bright);margin-top:8px}
.contact{height:122px;display:flex;flex-direction:column;justify-content:center;padding-left:70px;gap:3px}
.contact div{display:flex;align-items:center;gap:8px;color:var(--white);font-size:17px;font-weight:700;white-space:nowrap}

/* cover */
.logo{display:flex;flex-direction:column;align-items:center;justify-content:center}
.logo__name{font-family:var(--head);font-size:52px;color:var(--white);letter-spacing:4px;line-height:1}
.logo__sub{font-family:var(--body);font-weight:700;font-size:11px;letter-spacing:3px;color:var(--white);margin-top:6px}
.cover-top{height:120px}
.cover-band{height:153px;text-align:center;color:var(--white);padding-top:22px}
.cover-band .kicker{font-size:22px;letter-spacing:1px;display:flex;align-items:center;justify-content:center;gap:10px}
.cover-band .kicker::before,.cover-band .kicker::after{content:"";width:22px;height:2px;background:var(--white)}
.cover-band h1{font-family:var(--head);font-weight:400;font-size:42px;line-height:1}
.cover-photo{height:272px;background:linear-gradient(180deg,#b9bec6,#8d8f93 55%,#5b5e66)}
.perks{height:113px;background:var(--white);display:flex;align-items:center}
.perk{flex:1;text-align:center;font-size:11.5px;line-height:1.25;color:var(--ink);border-right:1px solid #c9ccd3;padding:2px 4px}
.perk:last-child{border-right:0}
.perk svg{display:block;margin:0 auto 5px}
.cover-foot{height:122px;text-align:center;display:flex;flex-direction:column;justify-content:center;align-items:center}
.phone-big{font-family:var(--head);font-size:34px;color:var(--white);letter-spacing:1px}
.web{color:var(--blue-bright);font-size:13px;letter-spacing:3.5px;margin-top:2px;white-space:nowrap}
.tag{color:#b9c0cc;font-size:9.5px;letter-spacing:1px;margin-top:6px;white-space:nowrap}

/* inside left */
.values{padding:26px 30px 0;text-align:center}
.rule-head{font-family:var(--head);font-weight:400;font-size:30px;color:var(--blue-bright);display:flex;align-items:center;justify-content:center;gap:14px}
.rule-head::before,.rule-head::after{content:"";width:44px;height:2px;background:var(--blue-bright)}
.values .sub{font-size:12px;font-weight:700;margin-top:6px}
.circles{display:flex;justify-content:center;gap:14px;margin-top:18px}
.circle{width:80px;height:80px;border-radius:50%;background:var(--blue-deep);border:7px solid var(--navy-2);box-shadow:0 0 0 3px var(--line);display:flex;align-items:center;justify-content:center}
.circle--on{background:var(--blue-bright)}
.vals{display:flex;justify-content:center;gap:6px;margin-top:18px}
.val{width:92px;font-size:12px;line-height:1.35}
.val b{display:block}
.values .note{font-size:12.5px;font-weight:700;margin-top:16px}
.story{padding:26px 32px 0;flex:1}
.story p{font-size:12.3px;line-height:1.62;text-align:justify;margin-top:14px}
.story p + p{margin-top:16px}
.inside-foot{padding:0 32px 20px}
.inside-foot .web{letter-spacing:3.5px;font-size:14px}
.inside-foot .tag{margin-top:4px}

/* solutions */
.solutions{width:733px;background:var(--white);display:flex;flex-direction:column}
.solutions__body{flex:1;padding:30px 30px 0 32px}
.solutions h2{font-family:var(--head);font-weight:400;font-size:37px;color:var(--ink)}
.cols{display:flex;gap:28px;margin-top:28px}
.col{flex:1}
.svc{margin-bottom:34px}
.svc h3{display:flex;align-items:center;gap:8px;font-family:var(--head);font-weight:400;font-size:18px;color:var(--blue-deep)}
.svc p{font-size:13.5px;line-height:1.3;margin-top:10px}
.svc ul{list-style:none;margin-top:12px;font-size:13.5px;line-height:1.35;text-transform:uppercase}
.svc li{padding-left:16px;position:relative}
.svc li::before{content:"";position:absolute;left:2px;top:5px;border-left:6px solid var(--blue);border-top:4px solid transparent;border-bottom:4px solid transparent}
.svc ul.two{columns:2;column-gap:10px}
.brand{display:flex;flex-direction:column;align-items:flex-start;margin-top:-4px}
.brand .logo__name{color:var(--ink);font-size:60px}
.brand .logo__sub{color:var(--ink);font-size:12px;letter-spacing:2.6px}
.solutions__foot{height:122px;display:flex}
.strip-photo{width:367px;background:linear-gradient(90deg,#3a3e48,#6d727c 50%,#2c3038)}
.strip-band{flex:1;display:flex;flex-direction:column;justify-content:center;align-items:center}
.strip-band .web{color:var(--white)}
.strip-band .tag{color:var(--ice)}
</style>
</head>
<body>

<section class="spread spread--outside">
  <div class="panel dark">
    <div class="trench">
      <div class="trench__row">
        <div class="badge"><b>24/7</b><span>EMERGENCY<br>SERVICE</span></div>
        <h2>Need a<br><em>Trenchless<br>Solution?</em></h2>
      </div>
      <p>Ask about our non-invasive solutions as an alternative to traditional replacement for sewer and storm drain systems.</p>
    </div>
    <div class="why">
      <h2>Why Choose KWT?</h2>
      <ul>
        <li>Family-oriented team</li>
        <li>Licensed &amp; insured professionals</li>
        <li>Residential &amp; commercial expertise</li>
        <li>Honest recommendations</li>
        <li>Quality workmanship</li>
        <li>Emergency service available</li>
        <li>Clean, respectful technicians</li>
      </ul>
      <p>One trusted company for plumbing<br>and sewer solutions</p>
      <div class="van ph" role="img" aria-label="Photo of the white company service van"></div>
    </div>
  </div>

  <div class="panel dark">
    <div class="start">
      <h2>READY TO<em>GET STARTED?</em></h2>
      <p class="lead">Whether it's a leaking pipe, a new water heater, a clogged drain, or a plumbing emergency, our team is here to help</p>
      <div class="testi">
        <h3>Testimonials</h3>
        <div class="quote">"This company is fantastic, very professional and knowledgeable. Use them at several of my communities I manage and highly recommend them!"<cite>Belmoro Townhomes</cite></div>
        <div class="quote">"KWT continues to be the primary plumbing vendor I use for all of my properties throughout Tampa Bay!"<cite>Corvallo Dunes Condominium</cite></div>
        <div class="quote">"KWT did a great job at a great price and have always been willing to help with their abundance of knowledge prior to even working on projects for our community!"<cite>Townhomes at Heron Pond</cite></div>
      </div>
    </div>
    <div class="contact band">
      <div><svg width="16" height="16" viewBox="0 0 24 24"><circle cx="12" cy="12" r="11" fill="#fff"/><path d="M8 6l2 0 1 3-1.5 1.2a8 8 0 0 0 4.3 4.3L15 13l3 1v2a2 2 0 0 1-2 2A10 10 0 0 1 6 8a2 2 0 0 1 2-2z" fill="#0054aa"/></svg>800-391-2857</div>
      <div><svg width="16" height="16" viewBox="0 0 24 24"><circle cx="12" cy="12" r="11" fill="#fff"/><rect x="6" y="8" width="12" height="8" rx="1" fill="#0054aa"/><path d="M6 8l6 5 6-5" stroke="#fff" stroke-width="1.3" fill="none"/></svg>info@kwtflowline.example</div>
      <div><svg width="16" height="16" viewBox="0 0 24 24"><circle cx="12" cy="12" r="10" fill="none" stroke="#fff" stroke-width="2"/><ellipse cx="12" cy="12" rx="4" ry="10" fill="none" stroke="#fff" stroke-width="1.6"/><path d="M2 12h20" stroke="#fff" stroke-width="1.6"/></svg>www.kwtflowline.example</div>
    </div>
  </div>

  <div class="panel panel--right dark">
    <div class="cover-top logo">
      <span class="logo__name">KWT</span>
      <span class="logo__sub">CONDUIT RENEWAL SERVICES</span>
    </div>
    <div class="cover-band band">
      <div class="kicker">TRADITIONAL</div>
      <h1>PLUMBING<br>SERVICES</h1>
    </div>
    <div class="cover-photo ph" role="img" aria-label="Photo of a plumbing technician working on pipes under a sink"></div>
    <div class="perks">
      <div class="perk"><svg width="30" height="28" viewBox="0 0 30 28"><rect x="4" y="4" width="22" height="22" fill="#0054aa"/><g fill="#fff"><rect x="8" y="8" width="4" height="4"/><rect x="18" y="8" width="4" height="4"/><rect x="8" y="15" width="4" height="4"/><rect x="18" y="15" width="4" height="4"/><rect x="13" y="20" width="4" height="6"/></g><rect x="2" y="2" width="26" height="3" fill="#0677ba"/></svg>Residential &amp;<br>commercial<br>Services</div>
      <div class="perk"><svg width="30" height="28" viewBox="0 0 30 28"><circle cx="14" cy="15" r="11" fill="none" stroke="#0677ba" stroke-width="3"/><path d="M14 8v7l5 3" stroke="#0054aa" stroke-width="2.4" fill="none"/></svg>24/7<br>Emergency<br>Service</div>
      <div class="perk"><svg width="30" height="28" viewBox="0 0 30 28"><rect x="6" y="2" width="17" height="23" rx="1" fill="#0054aa"/><g stroke="#fff" stroke-width="1.6"><path d="M9 8h11M9 12h11M9 16h7"/></g><circle cx="22" cy="21" r="5" fill="#0677ba"/></svg>Licensed<br>&amp; Insured<br>Services</div>
    </div>
    <div class="cover-foot">
      <div class="phone-big">800-391-2857</div>
      <div class="web">WWW.KWTFLOWLINE.EXAMPLE</div>
      <div class="tag">Reliable Repairs | Honest Service | Lasting Solutions</div>
    </div>
  </div>
</section>

<section class="spread spread--inside">
  <div class="panel dark">
    <div class="values">
      <h2 class="rule-head">Our Values</h2>
      <div class="sub">THE KWT WAY</div>
      <div class="circles">
        <div class="circle"><svg width="30" height="26" viewBox="0 0 30 26" fill="none" stroke="#fff" stroke-width="2"><circle cx="15" cy="8" r="4"/><circle cx="6" cy="11" r="3"/><circle cx="24" cy="11" r="3"/><path d="M8 24a7 7 0 0 1 14 0M1 22a5 5 0 0 1 6-5M29 22a5 5 0 0 0-6-5"/></svg></div>
        <div class="circle circle--on"><svg width="30" height="26" viewBox="0 0 30 26" fill="none" stroke="#fff" stroke-width="2"><rect x="3" y="3" width="24" height="15" rx="1"/><path d="M15 18v5M9 23h12"/></svg></div>
        <div class="circle"><svg width="30" height="30" viewBox="0 0 30 30" fill="none" stroke="#fff" stroke-width="2"><circle cx="15" cy="15" r="5"/><circle cx="15" cy="15" r="11" stroke-dasharray="4 3"/></svg></div>
      </div>
      <div class="vals">
        <div class="val"><b>Professional</b>Don't settle for good, BE GREAT</div>
        <div class="val"><b>Responsive</b>When there's a need, BE FIRST!</div>
        <div class="val"><b>Service</b>Life is not about you, BE ABOUT OTHERS!</div>
      </div>
      <div class="note">These three values guide everything we do</div>
    </div>
    <div class="story">
      <h2 class="rule-head">Our Story</h2>
      <p>Built on solving complex plumbing challenges. Trusted for every plumbing need. Since our founding, Conduit Renewal Services has built a reputation for solving complex plumbing and sewer problems through quality workmanship, professionalism, and innovative solutions. As our customers' needs have grown, so has our commitment to serving them.</p>
      <p>What began as a leader in pipe restoration has expanded into full-service plumbing, allowing us to provide complete solutions under one roof, from everyday repairs to major plumbing rehabilitation projects. Our business philosophy is a simple three-step approach: First, we listen to your needs Second, we identify the best solutions Third, we deliver the highest quality end result.</p>
    </div>
    <div class="inside-foot">
      <div class="web">WWW.KWTFLOWLINE.EXAMPLE</div>
      <div class="tag">Reliable Repairs | Honest Service | Lasting Solutions</div>
    </div>
  </div>

  <div class="solutions">
    <div class="solutions__body">
      <h2>Complete Plumbing Solutions</h2>
      <div class="cols">
        <div class="col">
          <div class="svc">
            <h3><svg width="22" height="22" viewBox="0 0 24 24" fill="none" stroke="#0677ba" stroke-width="2.2"><path d="M4 20l9-9M14 4a5 5 0 0 0 6 6l-3-3z"/></svg>Plumbing Repairs</h3>
            <p>Reliable solutions to keep your plumbing system running safely and efficiently.</p>
            <ul><li>Leak detection &amp; repair</li><li>Pipe burst repairs</li><li>Water line repairs</li><li>Whole-home repiping</li></ul>
          </div>
          <div class="svc">
            <h3><svg width="22" height="22" viewBox="0 0 24 24" fill="none" stroke="#0677ba" stroke-width="2.2"><path d="M4 4l16 16M20 4L4 20"/></svg>Fixtures &amp; Installations</h3>
            <p>Professional installation, repair, and replacement of the fixtures you use every day.</p>
            <ul class="two"><li>Faucets</li><li>Toilets</li><li>Sinks</li><li>Showers &amp; tubs</li><li>Garbage disposals</li><li>Hose bibs</li><li>Shut-off valves</li></ul>
          </div>
          <div class="brand">
            <span class="logo__name">KWT</span>
            <span class="logo__sub">CONDUIT RENEWAL SERVICES</span>
          </div>
        </div>
        <div class="col">
          <div class="svc">
            <h3><svg width="22" height="22" viewBox="0 0 24 24"><rect x="6" y="3" width="12" height="18" rx="2" fill="#0677ba"/><circle cx="12" cy="10" r="3" fill="#fff"/></svg>Water Heater Services</h3>
            <p>Whether you need a repair, replacement, or routine maintenance, we'll keep your hot water flowing.</p>
            <ul><li>Water heater repair</li><li>Water heater replacement</li><li>Tankless water heaters</li><li>Expansion tanks</li><li>Recirculation pumps</li><li>Preventative maintenance</li></ul>
          </div>
          <div class="svc">
            <h3><svg width="22" height="22" viewBox="0 0 24 24"><path d="M12 3c3 5 6 8 6 12a6 6 0 0 1-12 0c0-4 3-7 6-12z" fill="#0677ba"/></svg>Drain &amp; Sewer Solutions</h3>
            <p>From routine drain cleaning to complete sewer repairs, our team has the equipment and expertise to get your plumbing flowing again.</p>
            <ul><li>Drain cleaning</li><li>Hydro jetting</li><li>Camera inspections</li><li>Main sewer line cleaning</li><li>Sewer line repair</li><li>Sewer line replacement</li><li>Emergency drain backups</li></ul>
          </div>
        </div>
      </div>
    </div>
    <div class="solutions__foot">
      <div class="strip-photo ph" role="img" aria-label="Photo of water heater pipe fittings and valves"></div>
      <div class="strip-band band">
        <div class="phone-big">800-391-2857</div>
        <div class="web">WWW.KWTFLOWLINE.EXAMPLE</div>
        <div class="tag">Reliable Repairs | Honest Service | Lasting Solutions</div>
      </div>
    </div>
  </div>
</section>

</body>
</html>
```